Design refresh required for educational resources

A full redesign/refresh is required for an education resource kit.
The final outputs will include:
- Powerpoint slide template
- parent handout template
- overview template
- 2 different types of lesson plan templates (can be related but need to have some differences to distinguish between the two)
- 2 x branded labels for resources
- teacher 'intervention plan' summary sheet
- 'scope and sequence' document
Design needs to have a fun, modern feel, capturing elements of the New Zealand landscape, flora and/or fauna.
The resources will be used as part of a teaching kit for use in schools.
Please see attached files for existing samples of some of the above documents. Full content to be provided for successful applicant.
Please submit sample of one or two of the documents to bid for this work - enough so that I can see the overall design aesthetic you are proposing.
New Zealand teachers and parents of 5 year old children

```html
<!DOCTYPE html>
<html lang="en">
<head>
<meta charset="utf-8">
<title>Week 1 – Lesson 2 lesson plan</title>
<link href="https://fonts.googleapis.com/css2?family=Montserrat:wght@300;400;500;600;700&family=Sacramento&family=Cormorant+Garamond:wght@500&display=swap" rel="stylesheet">
<style>
:root{
  --bg:#ececec;
  --paper:#ffffff;
  --ink:#2b2b2b;
  --ink-soft:#3d3d3d;
  --olive:#7b7d55;
  --sage:#9fb39a;
  --gold:#c9b457;
  --title-brown:#6b5a12;
  --day-brown:#8b6a2e;
  --game-orange:#f47b30;
  --game-shadow:#c2561a;
  --tile-blue:#bcd3e0;
  --tile-peach:#e8a486;
  --tile-green:#9ccc96;
  --photo-top:#8f9f86;
  --photo-mid:#a9b79e;
  --photo-low:#7f7a45;
}
*{box-sizing:border-box;margin:0;padding:0}
html,body{width:900px;height:1200px;overflow:hidden;background:var(--bg)}
body{position:relative;font-family:'Montserrat',sans-serif;color:var(--ink)}
.page{position:absolute;width:676px;height:955px;background:var(--paper);transform:scale(0.5425);transform-origin:0 0;border:1px solid #dcdcdc;overflow:hidden}
.page--lesson{left:248.5px;top:58.6px}
.page--games{left:64.6px;top:622.8px}
.page--links{left:468.2px;top:622.8px}
.abs{position:absolute}
.body-copy{font-size:12.2px;line-height:15px;font-weight:300;color:var(--ink-soft)}
.body-copy b{font-weight:600;color:var(--ink)}
.label{font-size:14px;font-weight:400;color:var(--ink)}
.aim{font-size:12.2px;font-weight:600;color:var(--ink)}
.band{position:absolute;left:28px;width:620px;height:37px;background:var(--gold);border-radius:10px;color:#fff;font-size:23px;font-weight:500;text-align:center;line-height:37px;letter-spacing:.3px}
.objective{position:absolute;left:28px;width:620px;text-align:center;font-size:13.4px;font-weight:600;line-height:17px}
.divider{position:absolute;left:25px;width:625px;border-top:2px dotted #555}
.page-number{position:absolute;left:0;width:100%;top:930px;text-align:center;font-size:12px;font-weight:300}
.badge-game{position:absolute;width:62px;height:58px;border-radius:12px;background:var(--game-orange);box-shadow:-4px 4px 0 var(--game-shadow);transform:rotate(-22deg);color:#fff;font-weight:600;font-size:17px;line-height:58px;text-align:center;letter-spacing:.5px}
.figure{position:absolute;border-radius:40px}
.figure--child{background:linear-gradient(180deg,#f2c9a4 0%,#8fb6d9 45%,#e39a4c 100%)}
.figure--girl{background:linear-gradient(180deg,#b9834f 0%,#5f86b8 45%,#c2874b 100%)}
.figure--boy{background:linear-gradient(180deg,#8a5a33 0%,#e07560 40%,#4f6fa3 100%)}
.figure--kid{background:linear-gradient(180deg,#c78a4f 0%,#7c8fa3 45%,#c24d6b 100%)}
/* cover */
.hero{position:absolute;left:0;top:0;width:676px;height:242px;background:linear-gradient(180deg,var(--photo-top) 0%,var(--photo-mid) 18%,#b3bfa7 55%,#9ea889 78%,var(--photo-low) 100%)}
.brand{position:absolute;top:34px;height:60px;display:flex;align-items:center;gap:8px;color:#3a3a3a;font-family:'Montserrat',sans-serif;font-weight:600;font-size:11px;line-height:13px}
.brand-mark{width:26px;height:26px;border-radius:4px;background:#3a3a3a}
.brand-rule{position:absolute;left:122px;top:32px;width:1.5px;height:62px;background:#3a3a3a}
.week-title{position:absolute;left:462px;top:62px;display:flex;align-items:baseline;color:#3b3b34;white-space:nowrap}
.week-title__word{font-family:'Sacramento',cursive;font-size:76px;line-height:90px}
.week-title__number{font-family:'Cormorant Garamond',serif;font-size:44px;margin-left:14px}
.lesson-tab{position:absolute;left:28px;top:202px;width:197px;height:53px;background:var(--olive);border-radius:12px;color:#fff;font-size:34px;font-weight:400;line-height:53px;text-align:center;letter-spacing:.5px}
.book-label{position:absolute;left:28px;top:282px;font-size:21px;font-weight:300;color:#555}
.book-title{position:absolute;left:28px;top:308px;width:200px;font-size:22.5px;font-weight:600;line-height:27.5px;color:var(--title-brown)}
.book-authors{position:absolute;left:28px;top:404px;font-size:13.5px;font-weight:600;line-height:17px}
.info-box{position:absolute;left:239px;top:257px;width:409px;height:213px;background:var(--sage);border-radius:12px;padding:11px 12px;font-size:12.6px;font-weight:300;line-height:19px;letter-spacing:-.1px;color:#2f2f2f}
.info-box p{color:#fbfbf5;white-space:nowrap}
.info-box p.wrap{white-space:normal}
.info-box .key{color:#2f2f2f}
.badge-day{position:absolute;left:34px;top:568px;width:58px;height:54px;border-radius:12px;background:var(--day-brown);box-shadow:-3px 3px 0 #5e4518;transform:rotate(-22deg);color:#fff;font-weight:600;font-size:16px;line-height:54px;text-align:center}
/* links page */
.tile{position:absolute;top:28px;width:65px;height:62px;font-size:34px;font-weight:400;text-align:center;line-height:62px;color:#222}
.tile--d{left:110px;background:var(--tile-blue)}
.tile--o{left:204px;background:var(--tile-peach)}
.tile--t{left:298px;background:var(--tile-green)}
</style>
</head>
<body>

<section class="page page--lesson">
  <div class="hero" role="img" aria-label="Misty lake landscape with a person holding binoculars and two wooden chairs on a grassy shore"></div>
  <div class="brand" style="left:38px;width:80px;flex-direction:column;align-items:flex-start;gap:3px"><div class="brand-mark"></div><div>Kōwhai<br>Reading Path</div></div>
  <div class="brand-rule"></div>
  <div class="brand" style="left:134px;width:120px"><div>Southbridge<br>University</div></div>
  <div class="week-title"><span class="week-title__word">Week</span><span class="week-title__number">1</span></div>
  <div class="lesson-tab">LESSON 2</div>

  <div class="book-label">Book:</div>
  <div class="book-title">The Moonlit Party of Ruru and Kiwi</div>
  <div class="book-authors">by Hana Wilder<br>and Mere Tanner</div>

  <div class="info-box">
    <div class="key">Target vocabulary:</div>
    <p class="wrap">velvety, decorate, marama (moon), rākau (tree)<span class="key">Target phoneme/graphemes:</span> m, d</p>
    <div class="key">Target picture card words (English):</div>
    <p>mop, mat, mad, map, men, dog, dig, dad, dot, den</p>
    <div class="key">Target picture card words (te reo Māori):</div>
    <p>marama, manu, moe</p>
    <div class="key">Suggested readers:</div>
    <p>Pat, Tap; Pop, Pop in the Pot; Mot and Don; Dig the Mud</p>
  </div>

  <div class="band" style="top:484px">Vocabulary Development with Book</div>
  <div class="objective" style="top:530px">Objective: Learning about new words, developing listening and oral narrative skills</div>

  <div class="badge-day">DAY 2</div>
  <div class="abs label" style="left:112px;top:564px">Summarise the story:</div>
  <div class="abs body-copy" style="left:112px;top:583px;width:540px">Retell the story in summary form, using the pictures as prompts, be sure to include the pages with target vocabulary provide a definition of the word and use it in a sentence as per the postit note prompts.</div>

  <div class="abs body-copy" style="left:27px;top:643px;width:625px">Encourage children to help you retell the story. For example, <b>“This is a story about _______. Let’s remember what happened at the start of the story</b> (summarise the beginning). <b>Then what happened?”</b> Use appropriate pages from the story as you summarise. Support children with limited oral language skills by using the story book pictures as prompts. E.g., open a page of the story and ask <b>“what can we see on this page?”</b> Encourage any verbal response and use language elicitation and scaffolding strategies to extend children’s language.</div>

  <div class="band" style="top:750px">Phonological Awareness (PA) Skill Building</div>
  <div class="objective" style="top:795px;left:45px;width:590px">Objective: Identifying sounds in words (including words from story) and matching phoneme with grapheme.</div>
  <div class="abs label" style="left:28px;top:833px">Phoneme identity:</div>
  <div class="abs body-copy" style="left:28px;top:853px;width:620px">Bring children’s attention to the first sound in words. Write the week’s target sound on the board (or use a large letter card) and run through the picture cards associated with that target sound. Emphasise the target phoneme and grapheme in the word.</div>
  <div class="page-number">4</div>
</section>

<section class="page page--games">
  <div class="abs label" style="left:27px;top:27px">For example:</div>
  <div class="abs body-copy" style="left:27px;top:46px;width:625px"><b>“In our book this week, Ruru and Kiwi hosted a party with lots of dancing. Dance starts with a /d/ sound, and yesterday we talked about some other words that start with a /d/ sound, like dot and den and dog</b> (display the large letter card or write on the board). <b>Let’s write the letter together (write in the air or on whiteboards). What sound does it make? /d/! Now let’s listen to some words that start with a /d/ sound”.</b> Explicitly draw children’s attention to the target sound in the word as you work through the target /d/cards E.g., <b>“Dog starts with /d/ see the letter d at the beginning of the word, this letter makes the /d/ sound. Listen again for the /d/ at the start of dog.”</b> Revise the target /d/ cards: dog, dig, dad, dot, den.</div>

  <div class="divider" style="top:184px"></div>
  <div class="badge-game" style="left:32px;top:200px">GAME</div>
  <div class="figure figure--child" style="left:8px;top:278px;width:88px;height:122px" role="img" aria-label="Cartoon child jumping with arms outstretched"></div>
  <div class="abs label" style="left:110px;top:200px">Word Wizard:</div>
  <div class="abs body-copy" style="left:110px;top:220px;width:540px">Generate words that start with the target sound. You can do this as a class, or ask individual children for their own ideas. Write a few of the words on the board as you go, highlighting the initial target sound in each word. You could consider inviting children to go on a ‘sound hunt’ around the room, looking for objects or pictures that start with the target sound. If children are having difficulty thinking of /d/ words independently, increase your level of prompting so they are successful. E.g., <b>“I can see a desk – does desk start with a /d/ sound? Listen, ‘d-esk’. I think it does! What about ‘mat’? Let’s listen, ‘m-at’. No, I can’t hear a /d/ sound at the start of ‘mat’.</b></div>
  <div class="abs body-copy" style="left:110px;top:362px"><b>Aim for 6 words</b> that start with the /d/ sound.</div>
  <div class="abs label" style="left:110px;top:398px">Segmenting and Blending:</div>
  <div class="abs body-copy" style="left:110px;top:418px">Encourage children to segment and blend words using your chosen game.</div>

  <div class="divider" style="top:454px"></div>
  <div class="badge-game" style="left:32px;top:470px">GAME</div>
  <div class="figure figure--girl" style="left:20px;top:570px;width:72px;height:112px" role="img" aria-label="Cartoon girl waving with both arms raised"></div>
  <div class="abs label" style="left:109px;top:469px">Class Segmentation Boards:</div>
  <div class="abs body-copy" style="left:109px;top:489px;width:540px">Using a segmentation board on the whiteboard, segment target words and some words from the story. Say the word, and then demonstrate how to segment the word into phonemes by placing a token on a square each time you say a phoneme. Once segmented, blend the phonemes together to read the word. E.g., Target word: <b>“Listen for the sounds in duck: di-g, (representing each phoneme with a block or counter) dig there are three sounds in dig”.</b></div>
  <div class="abs body-copy" style="left:109px;top:585px;width:540px">After you’ve demonstrated a couple of words, work together as a class to segment words and then blend together again. Choose one of the words you have segmented to write on the board using segmentation skills e.g. <b>“I will write the word dog listen for the sounds as I write the word dog. This word says dog.”</b></div>
  <div class="abs aim" style="left:109px;top:668px">Aim for 6 items each, segmented and blended.</div>
  <div class="abs label" style="left:109px;top:703px">Sound manipulation:</div>
  <div class="abs body-copy" style="left:109px;top:723px">Support children to add, move and manipulate sounds in words using your chosen game.</div>

  <div class="divider" style="top:754px"></div>
  <div class="badge-game" style="left:34px;top:772px">GAME</div>
  <div class="abs label" style="left:111px;top:769px">On the Board:</div>
  <div class="abs body-copy" style="left:111px;top:789px;width:540px">Using the class whiteboard, complete a manipulation chain activity. Draw 34 large squares to use as spaces to write the letter/s (grapheme) that represent each phoneme in the word. Write the grapheme in each square, and start a manipulation chain, changing one letter each time.</div>
  <div class="abs body-copy" style="left:111px;top:870px;width:540px">E.g., Write ‘dot’ on the board in large squares, one letter per square. <b>“This says ‘dot’, let’s make it say ‘hot’. Which letter should I rub out?”</b></div>
  <div class="page-number">5</div>
</section>

<section class="page page--links">
  <div class="figure figure--boy" style="left:8px;top:26px;width:92px;height:100px" role="img" aria-label="Cartoon boy leaping with arms and legs spread"></div>
  <div class="tile tile--d">d</div>
  <div class="tile tile--o">o</div>
  <div class="tile tile--t">t</div>
  <div class="abs body-copy" style="left:110px;top:108px;width:545px"><b>“That’s right, we rub out the ‘d’ because the first sound changed. Let’s replace it with an ‘h’. Now it says ‘hot’. Let’s make it say ‘hat’.”</b></div>
  <div class="abs body-copy" style="left:110px;top:142px;width:545px">Continue on until 6 changes have been completed. Always explicitly draw attention to the letter, sound, and where the change in the word has happened. You may like to use a helper to rub out the letter and/or write new letters in, or run this as a teacherled activity.</div>
  <div class="abs label" style="left:110px;top:190px">Chain examples:</div>
  <div class="abs body-copy" style="left:110px;top:210px">dog&gt;dot&gt;pot&gt;mot&gt;mop&gt;top</div>
  <div class="abs body-copy" style="left:110px;top:228px">dot&gt;hot&gt;hat&gt;mat&gt;sat&gt;sit&gt;bit</div>
  <div class="abs aim" style="left:110px;top:264px">Aim for at least 1 manipulation chain with 6 sound changes.</div>
  <div class="abs label" style="left:110px;top:282px">Extension activity:</div>
  <div class="abs body-copy" style="left:110px;top:303px">Have children complete the chains individually, using personal whiteboards or paper.</div>

  <div class="band" style="top:329px;left:27px">Link to Reading and Writing</div>
  <div class="objective" style="top:375px">Objective: Transfer PA knowledge to a reading and spelling activity.</div>
  <div class="abs label" style="left:27px;top:405px">Reading and spelling game:</div>
  <div class="abs body-copy" style="left:27px;top:425px;width:620px">Use your chosen activity to explicitly link the skill building activities (identifying phonemes, blending and segmenting words) to a reading or writing activity.</div>

  <div class="divider" style="top:480px"></div>
  <div class="badge-game" style="left:34px;top:500px">GAME</div>
  <div class="figure figure--kid" style="left:20px;top:570px;width:78px;height:108px" role="img" aria-label="Cartoon child cheering with arms out"></div>
  <div class="abs label" style="left:110px;top:492px">Class/large group level Build a Sentence class:</div>
  <div class="abs body-copy" style="left:110px;top:512px;width:545px">Choose a theme or topic that relates to this week’s book and as a class build a simple sentence using skill building strategies. Try to use mostly regular, decodable words in the sentence. See the scope and sequence word bank on the session overview page for word choices in the carrier phrase. E.g., Write the carrier sentence on the board: The _______ danced. and read as a class. Fill in the carrier sentence with ideas from the class, segmenting out the word as you write. Choose simple, short animal names to start with.</div>
  <div class="abs body-copy" style="left:110px;top:623px;width:545px">E.g., <b>In our story lots of animals joined the part to dance and dine. Let’s write a sentence about some of the animals who joined the party.</b></div>
  <div class="abs body-copy" style="left:110px;top:655px">The frog danced. The grub danced. The bat danced.</div>
  <div class="abs aim" style="left:110px;top:692px">Aim for 6 sentences, read together as a class.</div>

  <div class="band" style="top:726px;left:27px">Link to Small Group Reading Instruction</div>
  <div class="objective" style="top:772px">Objective: Transfer skills to other literacy activities</div>
  <div class="abs label" style="left:27px;top:802px">Small group reading with suggested early reader (see separate lesson template):</div>
  <div class="abs body-copy" style="left:27px;top:822px;width:620px">Select an appropriate decodable text for children to read in a small group reading activity, following the separate lesson plan template.</div>
  <div class="abs body-copy" style="left:27px;top:873px">Suggested readers:</div>
  <div class="abs body-copy" style="left:27px;top:891px">Easier: Tap, Pat; Pop, Pop in the Pot</div>
  <div class="abs body-copy" style="left:27px;top:909px">Harder: Mot and Don; Dig the Mud</div>
  <div class="page-number" style="top:926px">6</div>
</section>

</body>
</html>
```